Business Card Design

We are looking for a double sided business card.

On one side would be our logo

On the Other Side

Martin Kolby
Sales and Marketing

Phone/Text Logo and 530-418-2763
Email Logo and info@plumvalepets.com
Website Logo and www.plumvalepets.com
Facebook Logo and plumvale pets
Instagram Logo and plumvale_pets

Target Market(s)

Pet owners

Contact Information for Business Card

In project description

Requirements
Must have
• Logo

```html
<!DOCTYPE html>
<html lang="en">
<head>
<meta charset="utf-8">
<title>Plumvale Pets – Business Card</title>
<link rel="stylesheet" href="https://fonts.googleapis.com/css2?family=Montserrat:wght@400;500;700;800&display=swap">
<style>
  :root {
    --stage: #2a2b2d;
    --card: #1c1c1d;
    --card-edge: #f08a12;
    --accent: #f39a1e;
    --text-light: #f2f2f2;
    --text-logo: #e4e4e4;
  }
  * { margin: 0; padding: 0; box-sizing: border-box; }
  html, body { width: 1200px; height: 811px; overflow: hidden; }
  body {
    background: var(--stage);
    font-family: "Montserrat", Arial, sans-serif;
    position: relative;
  }
  .card {
    position: absolute;
    width: 595px;
    height: 340px;
    background: var(--card);
    border-left: 3px solid var(--card-edge);
    border-bottom: 3px solid var(--card-edge);
    box-shadow: 0 10px 30px rgba(0,0,0,0.45);
  }
  .card--front { left: 170px; top: 45px; }
  .card--back { left: 435px; top: 425px; }

  .brand { text-align: center; }
  .brand__name {
    font-weight: 800;
    color: var(--text-logo);
    letter-spacing: 1px;
    line-height: 1;
  }
  .brand__url {
    margin-top: 10px;
    font-weight: 500;
    color: var(--accent);
    letter-spacing: 3px;
    text-transform: uppercase;
  }
  .card--front .brand {
    position: absolute;
    left: 0; right: 0; top: 120px;
  }
  .card--front .brand__name { font-size: 52px; }
  .card--front .brand__url { font-size: 11px; }

  .card--back .brand {
    position: absolute;
    right: 40px; top: 44px;
    width: 300px;
  }
  .card--back .brand__name { font-size: 34px; }
  .card--back .brand__url { font-size: 8px; margin-top: 8px; }

  .divider {
    position: absolute;
    left: 36px; right: 40px; top: 160px;
    height: 2px;
    background: var(--accent);
  }
  .person { position: absolute; left: 36px; top: 182px; }
  .person__name {
    font-size: 24px; font-weight: 800;
    color: var(--accent); text-transform: uppercase;
  }
  .person__role { font-size: 15px; color: var(--text-light); margin-top: 4px; }

  .contacts { position: absolute; left: 36px; top: 250px; list-style: none; }
  .contacts li, .socials li {
    display: flex; align-items: center; gap: 10px;
    font-size: 15px; color: var(--text-light);
    height: 24px;
  }
  .contacts svg { width: 15px; height: 15px; fill: var(--accent); flex: none; }

  .socials { position: absolute; right: 40px; top: 200px; list-style: none; }
  .socials li { justify-content: flex-end; }
  .social-dot {
    width: 12px; height: 12px; border-radius: 50%;
    background: var(--accent); flex: none;
  }
</style>
</head>
<body>
  <section class="card card--front">
    <div class="brand">
      <div class="brand__name">PLUMVALE PETS</div>
      <div class="brand__url">www.plumvalepets.com</div>
    </div>
  </section>

  <section class="card card--back">
    <div class="brand">
      <div class="brand__name">PLUMVALE PETS</div>
      <div class="brand__url">www.plumvalepets.com</div>
    </div>
    <div class="divider"></div>
    <div class="person">
      <div class="person__name">Martin Kolby</div>
      <div class="person__role">Sales and Marketing</div>
    </div>
    <ul class="contacts">
      <li>
        <svg viewBox="0 0 24 24" aria-hidden="true"><path d="M6.6 10.8a15.1 15.1 0 0 0 6.6 6.6l2.2-2.2c.3-.3.7-.4 1-.2 1.1.4 2.3.6 3.6.6.6 0 1 .4 1 1V20c0 .6-.4 1-1 1A17 17 0 0 1 3 4c0-.6.4-1 1-1h3.5c.6 0 1 .4 1 1 0 1.3.2 2.5.6 3.6.1.3 0 .7-.2 1z"/></svg>
        530-418-2763
      </li>
      <li>
        <svg viewBox="0 0 24 24" aria-hidden="true"><path d="M2 5h20v14H2z M3.5 6.5 12 13l8.5-6.5" fill="var(--accent)" stroke="var(--card)" stroke-width="1.6"/></svg>
        info@plumvalepets.com
      </li>
      <li>
        <svg viewBox="0 0 24 24" aria-hidden="true"><circle cx="12" cy="12" r="10"/><path d="M2 12h20M12 2c3 3 3 17 0 20M12 2c-3 3-3 17 0 20M4 7h16M4 17h16" fill="none" stroke="var(--card)" stroke-width="1.4"/></svg>
        www.plumvalepets.com
      </li>
    </ul>
    <ul class="socials">
      <li>plumvale pets <span class="social-dot"></span></li>
      <li>plumvale_pets <span class="social-dot"></span></li>
    </ul>
  </section>
</body>
</html>
```